Creative flyer for small business IT services

We are an IT services company based in Western Australia. We're looking to expand our market share amongst small businesses and need a brochure/flyer designed to give them a good overview of why we can help them. The design and layout should be consistent with an existing company profile brochure (included) but please be creative. A comprehensive brief with copy and a rough layout is included.

Small Business

```html
<!DOCTYPE html>
<html lang="en">
<head>
<meta charset="utf-8">
<title>Small Business IT Solutions – BrightNode</title>
<link rel="stylesheet" href="https://fonts.googleapis.com/css2?family=Source+Sans+3:wght@400;600;700&display=swap">
<style>
  :root {
    --brand-red: #a01d22;
    --backdrop: #857663;
    --paper: #ffffff;
    --panel-grey: #ebebeb;
    --ink: #2b2b2b;
    --ink-soft: #3a3a3a;
    --rule: #a01d22;
    --soil: #7a4a2a;
  }
  * { box-sizing: border-box; margin: 0; padding: 0; }
  html, body { width: 1200px; height: 900px; overflow: hidden; }
  body {
    background: var(--backdrop);
    font-family: "Source Sans 3", Arial, sans-serif;
    color: var(--ink);
    position: relative;
  }
  .flyer {
    position: absolute; left: 302px; top: 29px;
    width: 596px; height: 843px;
    background: var(--paper);
    overflow: hidden;
  }
  .masthead {
    position: absolute; left: 0; top: 0; width: 100%; height: 157px;
    background: var(--brand-red);
  }
  .masthead-title {
    position: absolute; left: 28px; top: 104px;
    color: #fff; font-weight: 400; font-size: 29px; letter-spacing: 0.2px;
  }
  .brand-mark { position: absolute; left: 481px; top: 36px; width: 76px; text-align: center; }
  .brand-square { display: block; width: 76px; height: 76px; background: #fff; }
  .brand-name { display: block; margin-top: 4px; color: #fff; font-size: 14px; font-weight: 400; }

  .hero-visual {
    position: absolute; left: 17px; top: 210px; width: 570px; height: 92px;
    background: linear-gradient(180deg, rgba(255,255,255,0) 0%, rgba(140,198,63,0.35) 45%, var(--soil) 100%);
  }
  .hero-copy { position: absolute; left: 28px; top: 185px; line-height: 22px; }
  .hero-copy .strong { font-weight: 700; font-size: 18.5px; color: var(--brand-red); display: block; }
  .hero-copy .light { font-weight: 400; font-size: 18.5px; color: var(--brand-red); display: block; }

  .intro { position: absolute; left: 28px; top: 322px; width: 320px; }
  .intro h2 { font-weight: 400; font-size: 17.5px; line-height: 19px; color: var(--brand-red); margin-bottom: 4px; }
  .intro p { font-size: 10.9px; line-height: 14px; color: var(--ink); }

  .reasons {
    position: absolute; left: 351px; top: 322px; width: 215px; height: 111px;
    background: var(--panel-grey); padding: 14px 12px 0 12px;
  }
  .reasons h3 { font-size: 7.6px; line-height: 10px; font-weight: 700; margin-left: 20px; margin-bottom: 4px; color: var(--ink); }
  .reasons ul { list-style: none; }
  .reasons li { display: flex; align-items: center; font-size: 7.6px; height: 16px; color: var(--ink); }
  .reasons svg { width: 12px; height: 11px; margin-right: 8px; flex: none; }

  .services { position: absolute; left: 22px; top: 443px; width: 550px; height: 316px; }
  .service { position: absolute; top: 0; width: 106px; height: 316px; }
  .service-tab {
    height: 22px; background: var(--panel-grey);
    color: var(--brand-red); font-weight: 700; font-size: 8.4px;
    display: flex; align-items: center; justify-content: center;
  }
  .service-body { margin-top: 4px; height: 290px; background: var(--panel-grey); padding: 6px 5px 0 5px; }
  .service-icon { display: block; margin: 0 auto 8px; height: 44px; }
  .service-body p { font-size: 7.3px; line-height: 10.1px; color: var(--ink-soft); margin-bottom: 7px; }

  .footer { position: absolute; left: 0; top: 768px; width: 100%; height: 42px; }
  .footer-brand { position: absolute; left: 32px; top: 11px; display: flex; align-items: center; }
  .footer-brand .square { width: 24px; height: 24px; background: var(--brand-red); margin-right: 6px; }
  .footer-brand .name { font-size: 14px; color: var(--ink); }
  .footer-divider { position: absolute; top: 6px; width: 1px; height: 32px; background: var(--rule); }
  .footer-text { position: absolute; top: 13px; font-size: 7.6px; line-height: 10px; text-align: center; color: var(--ink); }
  .footer-text strong { font-weight: 700; }
  .footer-phone { position: absolute; right: 36px; top: 11px; font-size: 14.5px; font-weight: 700; color: var(--ink); }
  .base-band { position: absolute; left: 0; bottom: 0; width: 100%; height: 22px; background: var(--brand-red); }
</style>
</head>
<body>
<article class="flyer">
  <header class="masthead">
    <h1 class="masthead-title">Small Business IT Solutions</h1>
    <div class="brand-mark">
      <span class="brand-square"></span>
      <span class="brand-name">brightnode</span>
    </div>
  </header>

  <div class="hero-visual" role="img" aria-label="Row of seedlings in mounds of soil, growing larger from left to right"></div>
  <div class="hero-copy">
    <span class="strong">Small business. Big ideas.</span>
    <span class="light">We’ll help your business grow.</span>
  </div>

  <section class="intro">
    <h2>We help small<br>businesses get ahead of the pack.</h2>
    <p>You’ve always got more to do. In a small business, the last thing you need is another hat to wear. You shouldn’t need to become a computer engineer to keep your business running smoothly. Say goodbye to IT headaches – our mission is to make your life easier.</p>
  </section>

  <aside class="reasons">
    <h3>Here’s why small<br>businesses love BrightNode:</h3>
    <ul>
      <li><svg viewBox="0 0 12 11"><path d="M1 6 L4.5 9.5 L11 1.5" fill="none" stroke="#a01d22" stroke-width="2.4"/></svg>We’re small business IT experts</li>
      <li><svg viewBox="0 0 12 11"><path d="M1 6 L4.5 9.5 L11 1.5" fill="none" stroke="#a01d22" stroke-width="2.4"/></svg>We speak plain English and won’t waste your time</li>
      <li><svg viewBox="0 0 12 11"><path d="M1 6 L4.5 9.5 L11 1.5" fill="none" stroke="#a01d22" stroke-width="2.4"/></svg>We care about our relationships</li>
      <li><svg viewBox="0 0 12 11"><path d="M1 6 L4.5 9.5 L11 1.5" fill="none" stroke="#a01d22" stroke-width="2.4"/></svg>We worry about IT so you don’t have to</li>
    </ul>
  </aside>

  <section class="services">
    <div class="service" style="left:0">
      <div class="service-tab">Support Services</div>
      <div class="service-body">
        <svg class="service-icon" viewBox="0 0 70 44" width="70">
          <circle cx="12" cy="14" r="8" fill="#a01d22"/>
          <rect x="12" y="11" width="50" height="6" rx="3" fill="#a01d22"/>
          <rect x="10" y="27" width="14" height="8" rx="2" fill="#a01d22"/>
          <rect x="24" y="29" width="40" height="4" rx="2" fill="#a01d22"/>
        </svg>
        <p>Say goodbye to IT interruptions, slow services, confusing jargon and inexplicable errors. We have solutions to your IT problems, and packages to suit every budget. We can even come to your workplace. If you run into a problem or need something done, just contact our Service Desk.</p>
        <p>Whether you have a single computer or a big team with complex requirements, our expert team can assist. We’ll give you an entire IT department for a fraction of the cost.</p>
      </div>
    </div>

    <div class="service" style="left:110px">
      <div class="service-tab">Monitoring &amp; Backup</div>
      <div class="service-body">
        <svg class="service-icon" viewBox="0 0 70 44" width="70">
          <rect x="22" y="2" width="42" height="40" rx="4" fill="#a01d22"/>
          <rect x="40" y="14" width="24" height="2" fill="#fff"/>
          <rect x="40" y="26" width="24" height="2" fill="#fff"/>
          <circle cx="30" cy="21" r="10" fill="#fff" stroke="#a01d22" stroke-width="3"/>
          <line x1="23" y1="28" x2="8" y2="42" stroke="#a01d22" stroke-width="4" stroke-linecap="round"/>
        </svg>
        <p>Most of us insure our cars and homes, yet small businesses often don’t protect themselves from the kind of disaster that strikes every day. Could your business recover from the complete loss of every electronic file – financial records, legal documents, customer information, intellectual property, archives, emails and more?</p>
        <p>Our Watch &amp; Shield solutions keep you safe from physical threats like theft, fire and floods, but also from electronic threats like viruses and hackers. Best of all – it happens automatically, so you can relax.</p>
      </div>
    </div>

    <div class="service" style="left:220px">
      <div class="service-tab">Hardware &amp; Software</div>
      <div class="service-body">
        <svg class="service-icon" viewBox="0 0 70 44" width="70">
          <rect x="4" y="10" width="14" height="24" rx="2" fill="#a01d22"/>
          <rect x="8" y="15" width="5" height="4" fill="#fff"/>
          <rect x="8" y="25" width="5" height="4" fill="#fff"/>
          <rect x="20" y="8" width="46" height="28" rx="3" fill="#a01d22"/>
          <path d="M30 22 h28 M50 17 l8 5 l-8 5" fill="none" stroke="#fff" stroke-width="1.8"/>
        </svg>
        <p>Every business needs the right tools for the job. We supply world class hardware and software products from Corvane, Lumetra, Baxtor, Orchard, Netrie, Inkwell, Voltek and many more. Our strong partnerships and buying power mean we can save you money.</p>
        <p>From a single keyboard to an entire infrastructure, we always take the time to help you select the right products.</p>
      </div>
    </div>

    <div class="service" style="left:329px">
      <div class="service-tab">Audit</div>
      <div class="service-body">
        <svg class="service-icon" viewBox="0 0 70 44" width="70">
          <rect x="8" y="4" width="50" height="34" rx="3" fill="none" stroke="#a01d22" stroke-width="4"/>
          <circle cx="32" cy="20" r="9" fill="#fff" stroke="#a01d22" stroke-width="3.5"/>
          <line x1="39" y1="27" x2="62" y2="40" stroke="#a01d22" stroke-width="4.5" stroke-linecap="round"/>
        </svg>
        <p>It helps to know where you stand.</p>
        <p>Get a clearer picture of your IT systems with our obligation-free IT audit and consultation.</p>
        <p>Contact us today and we’ll provide you with expert insights into how your business can benefit from today’s amazing technology.</p>
      </div>
    </div>

    <div class="service" style="left:439px">
      <div class="service-tab">Testimonials</div>
      <div class="service-body">
        <svg class="service-icon" viewBox="0 0 70 44" width="70">
          <path d="M11 3 h48 a3 3 0 0 1 3 3 v24 a3 3 0 0 1 -3 3 h-36 l-10 9 v-9 h-2 a3 3 0 0 1 -3 -3 v-24 a3 3 0 0 1 3 -3 z" fill="none" stroke="#a01d22" stroke-width="3.5" stroke-linejoin="round"/>
        </svg>
        <p>Don’t just take our word for it! Here’s what some satisfied customers have to say about BrightNode:</p>
        <p>“We are pleased to have BrightNode as part of our team. I recommend BrightNode for any business seeking a trustworthy, reliable and effective IT service provider.” Sam Ortega, Coastline Imaging</p>
        <p>“BrightNode’s expertise has allowed us to test, analyse and improve the reliability and performance of our application, further improving the health and financial status of our business.” Lena Marsh, Tallyline</p>
      </div>
    </div>
  </section>

  <footer class="footer">
    <div class="footer-brand"><span class="square"></span><span class="name">brightnode</span></div>
    <span class="footer-divider" style="left:151px"></span>
    <p class="footer-text" style="left:163px;width:120px">Level 12, 80 Harbour Row<br>Kestrel Bay WA 6112</p>
    <span class="footer-divider" style="left:297px"></span>
    <p class="footer-text" style="left:306px;width:130px">hello@brightnode.com.au<br><strong>www.brightnode.com.au</strong></p>
    <span class="footer-divider" style="left:441px"></span>
    <p class="footer-phone">1300 555 018</p>
  </footer>
  <div class="base-band"></div>
</article>
</body>
</html>
```